Personal Injury Billboard for a law frim

Our firm has a billboard we need art for. It will specifically for personal injury cases. The dimensions of art the billboard are 9 ft high 29 feet wide.

We want to highlight the terms, "Serious Injuries" and "Trusted. Local. Experienced." We want to incorporate the attached "Brightvale Honors" badge as well as our attached firm logo. We want the blue color scheme (see attached).

Maybe an image of an industrial plant in the background?

Sans Serif

```html
<!DOCTYPE html>
<html lang="en">
<head>
<meta charset="utf-8">
<title>Serious Injuries Billboard – Hollis Marrow Dane Attorneys</title>
<link rel="stylesheet" href="https://fonts.googleapis.com/css2?family=Michroma&family=Montserrat:wght@500;600&display=swap">
<style>
  :root {
    --page-bg: #e9ecf2;
    --board-blue: #1f3f8c;
    --board-blue-deep: #152f6e;
    --plant-haze: #3a5597;
    --ink-light: #ffffff;
    --badge-white: #ffffff;
    --badge-blue: #1d5fae;
    --badge-orange: #f39a1e;
    --badge-red: #b41f2e;
    --badge-grey: #4a4a4a;
  }
  * { margin: 0; padding: 0; box-sizing: border-box; }
  html, body {
    width: 1200px;
    height: 879px;
    overflow: hidden;
    background: var(--page-bg);
  }
  .canvas {
    position: relative;
    width: 1200px;
    height: 879px;
    display: flex;
    align-items: center;
  }
  .billboard {
    position: relative;
    width: 1200px;
    height: 372px;
    background: var(--board-blue);
    overflow: hidden;
  }
  .billboard__backdrop {
    position: absolute;
    inset: 0;
    background:
      linear-gradient(180deg, rgba(31,63,140,0.55) 0%, rgba(31,63,140,0.85) 100%),
      linear-gradient(90deg, var(--plant-haze) 0%, var(--board-blue-deep) 45%, var(--plant-haze) 75%, var(--board-blue-deep) 100%);
  }
  .firm {
    position: absolute;
    left: 60px;
    top: 110px;
    width: 360px;
    color: var(--ink-light);
    font-family: "Montserrat", sans-serif;
    font-weight: 600;
    text-align: center;
  }
  .firm__mark {
    display: flex;
    align-items: center;
    justify-content: center;
    gap: 16px;
    font-size: 52px;
    letter-spacing: 0.12em;
  }
  .firm__square {
    width: 40px;
    height: 40px;
    background: var(--ink-light);
  }
  .firm__url {
    margin-top: 22px;
    font-size: 19px;
    text-decoration: underline;
    letter-spacing: 0.01em;
  }
  .firm__name {
    margin-top: 6px;
    font-size: 21px;
    letter-spacing: 0.04em;
  }
  .firm__practice {
    margin-top: 4px;
    font-size: 13px;
    letter-spacing: 0.3em;
  }
  .headline {
    position: absolute;
    left: 440px;
    top: 40px;
    width: 720px;
    color: var(--ink-light);
    font-family: "Michroma", sans-serif;
    font-size: 47px;
    line-height: 70px;
    text-align: center;
    letter-spacing: 0.01em;
  }
  .honors {
    position: absolute;
    left: 582px;
    top: 274px;
    display: flex;
    gap: 7px;
  }
  .honors__badge {
    position: relative;
    width: 102px;
    height: 88px;
    background: var(--badge-white);
    border: 2px solid #d7d7d7;
  }
  .honors__badge::after {
    content: "";
    position: absolute;
    left: 0; right: 0; bottom: 0;
    height: 20px;
  }
  .honors__badge--selected::after { background: var(--badge-grey); }
  .honors__badge--blue { background: var(--badge-blue); }
  .honors__badge--blue::after { background: var(--badge-white); }
  .honors__badge--top::before {
    content: "";
    position: absolute;
    left: 0; right: 0; top: 38px;
    height: 30px;
    background: var(--badge-orange);
  }
  .honors__badge--years::before {
    content: "";
    position: absolute;
    left: 4px; right: 4px; top: 40px;
    height: 20px;
    background: var(--badge-red);
  }
</style>
</head>
<body>
<main class="canvas">
  <section class="billboard" aria-label="Personal injury billboard">
    <div class="billboard__backdrop" role="img" aria-label="Industrial plant with smokestacks under a blue tint"></div>

    <div class="firm">
      <div class="firm__mark"><span class="firm__square"></span>HMD</div>
      <p class="firm__url">www.hmd-legal.com</p>
      <p class="firm__name">HOLLIS MARROW DANE</p>
      <p class="firm__practice">ATTORNEYS</p>
    </div>

    <h1 class="headline">Serious Injuries<br>Trusted. Local.<br>Experienced</h1>

    <div class="honors" aria-label="Brightvale Honors badges">
      <div class="honors__badge honors__badge--selected"></div>
      <div class="honors__badge honors__badge--blue"></div>
      <div class="honors__badge honors__badge--top"></div>
      <div class="honors__badge honors__badge--years"></div>
    </div>
  </section>
</main>
</body>
</html>
```